Redesign of existing site - Velbrin GmbH

Redesign of the following site.
https://www.velbrin-gmbh.example/

The colors red and green need to remain.
Topic: calendar binder

The font "FF Market Regular" should be used s well. But -- if you find a font which is similar and a bit more modern, then go with it. (see font-example.jpg)

The mainpage should have a slider with a video first. Enclosed is a screenshot of the video. (see video.jpg)

Logo also enclosed as svg. The red color might not be quit right. Please check it on your own.
For the second page this page should be used to redesign:
https://www.velbrin-gmbh.example/bindungen/ring-wire-bindung/

I am planing to use the DIVI builder. If you built this in DIVI builder and be able to send me the template or installation (Duplicator) that would be a huge advantage.
Updates

IMPORTANT:
I have received many designs in English. But I can't present them to the customer. Please convert them into German, otherwise they cannot be used.

Requirements
Must have
• Please translate designs into german if it is to be considered. How should I explain a design in english to the customer?

```html
<!DOCTYPE html>
<html lang="de">
<head>
<meta charset="utf-8">
<title>Velbrin GmbH – Kalenderbindungen</title>
<link href="https://fonts.googleapis.com/css2?family=Bebas+Neue&family=Kalam:wght@700&family=Permanent+Marker&family=Poppins:wght@400;500;600&display=swap" rel="stylesheet">
<style>
:root{
  --red:#e5322a;
  --green:#66bb2e;
  --green-soft:#eef7e9;
  --ink:#1a1a1a;
  --text:#333;
  --dark:#1c1c1c;
  --white:#fff;
  --head:'Bebas Neue',sans-serif;
  --hand:'Permanent Marker','Kalam',sans-serif;
  --body:'Poppins',sans-serif;
}
*{box-sizing:border-box;margin:0;padding:0}
html,body{width:1200px;height:3690px;overflow:hidden}
body{font-family:var(--body);color:var(--text);background:var(--white);position:relative}
a{color:inherit;text-decoration:none}
.btn{display:inline-block;background:var(--red);color:var(--white);font-family:var(--body);font-size:11px;font-weight:600;text-transform:uppercase;padding:0 22px;line-height:43px;letter-spacing:.3px}
section,header,footer{position:absolute;left:0;width:1200px}
.hand{font-family:var(--hand);font-weight:400;font-style:italic}

/* Kopfbereich */
.site-header{top:0;height:62px;background:var(--white);border-bottom:1px solid #eee}
.brand{position:absolute;left:122px;top:8px;font-family:var(--head);font-size:46px;color:var(--red);line-height:46px;letter-spacing:-1px}
.nav{position:absolute;right:240px;top:0;display:flex;gap:28px;height:62px;align-items:center}
.nav a{font-size:11px;font-weight:500;color:var(--ink);text-transform:uppercase}
.nav a.active{color:var(--red);border-bottom:1px solid var(--red);padding-bottom:3px}
.nav a .caret{font-size:8px;color:var(--red);margin-left:3px}
.site-header .btn{position:absolute;right:122px;top:14px;line-height:33px;padding:0 17px}

/* Hero */
.hero{top:62px;height:514px;background:linear-gradient(90deg,#f4f4f4 0%,#e9e9e9 50%,#d6d6d6 100%)}
.hero-kicker{position:absolute;left:122px;top:90px;font-size:18px;color:var(--ink);display:flex;align-items:center;gap:14px}
.hero-kicker::after{content:"";width:98px;height:1px;background:var(--red)}
.hero h1{position:absolute;left:120px;top:124px;font-family:var(--head);font-weight:400;font-size:74px;line-height:70px;color:var(--ink);letter-spacing:1px}
.hero p{position:absolute;left:122px;top:272px;width:410px;font-size:11.5px;line-height:18px}
.hero .btn{position:absolute;left:122px;top:350px}
.hero-visual{position:absolute;left:690px;top:20px;width:510px;height:494px;background:linear-gradient(135deg,#cfd8d3 0%,#7fa07a 40%,#2c5a34 65%,#c9ccd3 100%);clip-path:polygon(22% 18%,80% 0,100% 8%,100% 88%,58% 100%,2% 72%)}

/* Leistungen */
.services{top:576px;height:476px}
.section-title{font-family:var(--head);font-weight:400;color:var(--ink);text-align:center;letter-spacing:.5px}
.services .section-title{position:absolute;top:56px;width:100%;font-size:52px}
.services .lead{position:absolute;left:280px;top:118px;width:640px;text-align:center;font-size:11.5px;line-height:18px}
.service-card{position:absolute;top:200px;width:306px;height:138px;border:1px solid var(--red);background:var(--white);padding:20px 14px 0 108px}
.service-card .icon{position:absolute;left:20px;top:18px;width:70px;height:70px}
.service-card h3{font-size:16px;color:var(--ink);margin:6px 0 8px;line-height:20px}
.service-card p{font-size:10.5px;line-height:13.5px}
.arrow-btn{position:absolute;width:40px;height:40px;border:1.5px solid var(--green);border-radius:50%;background:var(--white)}
.arrow-btn svg{position:absolute;left:12px;top:12px}
.services .btn{position:absolute;left:50%;transform:translateX(-50%);top:369px}

/* Über uns */
.about{top:1052px;height:423px;background:var(--green-soft)}
.about h2{position:absolute;left:122px;top:73px;font-family:var(--head);font-weight:400;font-size:52px;color:var(--ink);display:flex;align-items:center;gap:10px}
.about h2::after{content:"";width:92px;height:1px;background:var(--red);margin-top:-6px}
.about p{position:absolute;left:122px;top:134px;width:330px;font-size:11.5px;line-height:17.5px}
.about .btn{position:absolute;left:122px;top:319px}
.photo-team{position:absolute;left:669px;top:63px;width:408px;height:297px;background:linear-gradient(135deg,#d7c6a8 0%,#8f7d66 45%,#3a3532 100%)}
.photo-spiral{position:absolute;left:516px;top:131px;width:213px;height:200px;background:linear-gradient(135deg,#f2f2f2 0%,#c9843c 50%,#3b3b3b 100%);border:5px solid var(--white)}
.about-mark{position:absolute;left:1078px;top:80px;font-family:var(--head);font-size:118px;color:#d8ecca;writing-mode:vertical-rl;line-height:118px;letter-spacing:2px}

/* Bindungen */
.bindings{top:1475px;height:498px}
.bindings .section-title{position:absolute;top:58px;width:100%;font-size:50px}
.bindings .lead{position:absolute;top:118px;width:100%;text-align:center;font-size:11.5px}
.binding-card{position:absolute;top:176px;width:175px;height:258px;border-left:4px solid var(--green)}
.binding-card .thumb{height:193px;margin-left:-4px}
.binding-card h3{font-size:16px;color:var(--ink);margin:14px 0 4px 14px;white-space:nowrap}
.binding-card a{margin-left:14px;font-size:10.5px;font-weight:600;color:var(--red);text-decoration:underline}

/* Kennzahlen */
.stats{top:1973px;height:335px;background:var(--dark);overflow:hidden}
.stats .waves{position:absolute;left:0;top:0}
.stat{position:absolute;top:57px;width:190px;text-align:center}
.stat svg{display:block;margin:0 auto}
.stat .over{position:absolute;top:62px;width:190px;font-size:20px;color:var(--red)}
.stat .num{position:absolute;top:88px;width:190px;font-size:44px;font-weight:500;color:var(--red);line-height:50px}
.stat .num small{font-size:22px;margin-right:8px}
.stat .num .unit{font-size:19px}
.stat .label{margin-top:20px;font-size:18px;color:var(--white);white-space:nowrap}

/* Galerie */
.gallery{top:2308px;height:778px}
.gallery .section-title{position:absolute;top:56px;width:100%;font-size:52px}
.tabs{position:absolute;left:295px;top:122px;width:614px;border-bottom:1px solid var(--red);height:26px}
.tabs span{position:absolute;top:0;font-size:13px;color:var(--ink)}
.tabs span.active{color:var(--green)}
.tabs span.active::after{content:"";position:absolute;left:-24px;right:-26px;bottom:-9px;height:3px;background:var(--green)}
.tile{position:absolute;width:146px}
.tile .thumb{height:157px}
.tile h4{font-size:13px;color:var(--ink);margin-top:10px;line-height:17px}
.tile p{font-size:11px;line-height:17px}
.gallery .btn{position:absolute;left:50%;transform:translateX(-50%);top:673px}

/* Aufruf */
.cta{top:3086px;height:294px;background:var(--green);overflow:hidden}
.cta h2{position:absolute;top:60px;width:100%;text-align:center;font-family:var(--head);font-weight:400;font-size:53px;line-height:56px;color:var(--white);letter-spacing:.5px}
.cta .btn{position:absolute;left:50%;transform:translateX(-50%);top:187px}

/* Fußbereich */
.site-footer{top:3380px;height:310px;background:var(--dark);color:var(--white)}
.site-footer .brand{top:63px;left:122px}
.footer-about{position:absolute;left:122px;top:120px;width:145px;font-size:10.5px;line-height:15px}
.fcol{position:absolute;top:70px}
.fcol h5{font-family:var(--head);font-weight:400;font-size:17px;letter-spacing:.5px;margin-bottom:18px}
.fcol ul{list-style:none}
.fcol li{font-size:10.5px;margin-bottom:10px}
.contact li,.social li{display:flex;align-items:center;gap:14px;margin-bottom:12px}
.ico{width:24px;height:24px;border:1px solid var(--red);display:flex;align-items:center;justify-content:center}
.newsletter .field{width:212px;height:43px;border:1px solid var(--red);font-size:11px;padding:14px 12px}
.newsletter .btn{display:block;width:212px;text-align:center;margin-top:8px}
.footer-bar{position:absolute;left:122px;top:272px;width:956px;border-top:1px solid #444;padding-top:8px;font-size:10px;display:flex;justify-content:space-between}
.footer-bar nav a{margin-left:14px}
</style>
</head>
<body>

<header class="site-header">
  <div class="brand">VELBRIN</div>
  <nav class="nav">
    <a class="active" href="#">Start</a>
    <a href="#">Unternehmen<span class="caret">▾</span></a>
    <a href="#">Bindungen<span class="caret">▾</span></a>
    <a href="#">Exklusiv<span class="caret">▾</span></a>
    <a href="#">Galerie<span class="caret">▾</span></a>
    <a href="#">Service<span class="caret">▾</span></a>
  </nav>
  <a class="btn" href="#">Kontakt</a>
</header>

<section class="hero">
  <div class="hero-kicker">WILLKOMMEN BEI</div>
  <h1>VELBRIN<br>KALENDERBINDUNGEN</h1>
  <p>Das Unternehmen wurde am 1. Juni 1954 von der Familie Velbrin gegründet, mit Schreibwaren und Kalenderherstellung als Kerngeschäft. Damals wurden Kalender noch von Hand in Heimarbeit gebunden.</p>
  <a class="btn" href="#">Mehr erfahren</a>
  <div class="hero-visual" role="img" aria-label="Tischkalender mit Ring-Wire-Bindung und Blumenfoto"></div>
</section>

<section class="services">
  <h2 class="section-title">SERVICE AUS EINER HAND – KOMPETENZ VERBINDET!</h2>
  <p class="lead">Velbrin – der Name steht für höchste Qualität und Erfahrung bei allen flachliegenden Kalender- und Broschürenbindungen. Seit über 50 Jahren beraten wir Kunden im In- und Ausland kreativ in allen Fragen rund um Gestaltung und Funktion ihrer Produkte.</p>

  <div class="arrow-btn" style="left:58px;top:242px"><svg width="14" height="14" viewBox="0 0 14 14"><path d="M9 2L4 7l5 5" fill="none" stroke="#e5322a" stroke-width="2"/></svg></div>
  <div class="arrow-btn" style="left:1100px;top:242px"><svg width="14" height="14" viewBox="0 0 14 14"><path d="M5 2l5 5-5 5" fill="none" stroke="#e5322a" stroke-width="2"/></svg></div>

  <article class="service-card" style="left:122px">
    <svg class="icon" viewBox="0 0 70 70"><circle cx="35" cy="35" r="33" fill="none" stroke="#66bb2e" stroke-width="4"/><circle cx="35" cy="35" r="25" fill="#eef7e9"/><circle cx="35" cy="32" r="10" fill="none" stroke="#e5322a" stroke-width="2"/><path d="M29 41l-3 9 9-4 9 4-3-9" fill="none" stroke="#e5322a" stroke-width="2"/></svg>
    <h3 class="hand">EXKLUSIV</h3>
    <p>Außergewöhnliche Aufgaben sind unsere Spezialität – Exklusivität ist unser Markenzeichen.</p>
  </article>
  <article class="service-card" style="left:447px">
    <svg class="icon" viewBox="0 0 70 70"><circle cx="35" cy="35" r="33" fill="none" stroke="#66bb2e" stroke-width="4"/><circle cx="35" cy="35" r="25" fill="#eef7e9"/><circle cx="35" cy="28" r="5" fill="none" stroke="#e5322a" stroke-width="2"/><circle cx="24" cy="32" r="4" fill="none" stroke="#e5322a" stroke-width="2"/><circle cx="46" cy="32" r="4" fill="none" stroke="#e5322a" stroke-width="2"/><path d="M25 46c0-6 4-10 10-10s10 4 10 10z" fill="none" stroke="#e5322a" stroke-width="2"/></svg>
    <h3 class="hand">UNSER TEAM</h3>
    <p>Seit über 50 Jahren beraten wir Kunden im In- und Ausland mit Ideen in allen Fragen zu Gestaltung und Funktion ihrer Produkte.</p>
  </article>
  <article class="service-card" style="left:772px">
    <svg class="icon" viewBox="0 0 70 70"><circle cx="35" cy="35" r="33" fill="none" stroke="#66bb2e" stroke-width="4"/><circle cx="35" cy="35" r="25" fill="#eef7e9"/><circle cx="35" cy="35" r="13" fill="none" stroke="#e5322a" stroke-width="2"/><path d="M35 30v1M35 34v9" stroke="#e5322a" stroke-width="2.5"/></svg>
    <h3 class="hand">TECHNISCHE INFOS</h3>
    <p>Wenn es ins Detail geht, helfen wir Ihnen gern. So präsentieren Sie Ihre Produkte bestmöglich.</p>
  </article>

  <a class="btn" href="#">Alle Leistungen</a>
</section>

<section class="about">
  <h2>ÜBER UNS</h2>
  <p>Die Industriebuchbinderei Velbrin GmbH + Co. KG bietet Ihnen individuelle und ganzheitliche Lösungen für vielfältige Anforderungen in ihrer Kernkompetenz „Welt der Bindung“. Mit viel Erfahrung und Kreativität beraten wir Sie gern. Unser Angebot reicht von Planung und Produktion bis zum individuellen Versand an Ihre Kunden. Bücher, Broschüren, Tisch- und Wandkalender – Design und Funktion lassen sich perfekt verbinden.</p>
  <a class="btn" href="#">Mehr erfahren</a>
  <div class="photo-team" role="img" aria-label="Zwei Kollegen prüfen gedruckte Kalenderblätter am Tisch"></div>
  <div class="photo-spiral" role="img" aria-label="Nahaufnahme einer orangefarbenen Ring-Wire-Bindung"></div>
  <div class="about-mark">VELBRIN</div>
</section>

<section class="bindings">
  <h2 class="section-title">BLÄTTERN LEICHT GEMACHT!</h2>
  <p class="lead">Unsere Kalenderbindungen und Bindungen auf einen Blick.</p>
  <div class="arrow-btn" style="left:58px;top:254px"><svg width="14" height="14" viewBox="0 0 14 14"><path d="M9 2L4 7l5 5" fill="none" stroke="#e5322a" stroke-width="2"/></svg></div>
  <div class="arrow-btn" style="left:1100px;top:254px"><svg width="14" height="14" viewBox="0 0 14 14"><path d="M5 2l5 5-5 5" fill="none" stroke="#e5322a" stroke-width="2"/></svg></div>

  <article class="binding-card" style="left:122px"><div class="thumb" role="img" aria-label="Orangefarbene Ring-Wire-Bindung" style="background:linear-gradient(135deg,#e9e9e9,#c7772e 50%,#2e2e2e)"></div><h3 class="hand">RING-WIRE-BINDUNG</h3><a href="#">MEHR ERFAHREN</a></article>
  <article class="binding-card" style="left:316px"><div class="thumb" role="img" aria-label="Schwarze Spiralbindung" style="background:linear-gradient(135deg,#f4f4f4,#b9c0c6 50%,#3a3a3a)"></div><h3 class="hand">SPIRALBINDUNG</h3><a href="#">MEHR ERFAHREN</a></article>
  <article class="binding-card" style="left:511px"><div class="thumb" role="img" aria-label="Rote Leinenfalz-Rücken" style="background:linear-gradient(160deg,#f0f0f0,#c8262a 45%,#e8e8e8)"></div><h3 class="hand">LEINENFALZ</h3><a href="#">MEHR ERFAHREN</a></article>
  <article class="binding-card" style="left:707px"><div class="thumb" role="img" aria-label="Blau-weiße gefalzte Tischkarte" style="background:linear-gradient(160deg,#f5f5f5 40%,#2b6fd0 75%,#dfe3e8)"></div><h3 class="hand">FALZNAHT</h3><a href="#">MEHR ERFAHREN</a></article>
  <article class="binding-card" style="left:902px"><div class="thumb" role="img" aria-label="Grüne Kalenderblöcke mit Sprungbindung" style="background:linear-gradient(90deg,#f2f2f2,#2f8a3e 30%,#1f6a2e 70%,#eaeaea)"></div><h3 class="hand">SPRUNGBINDUNG</h3><a href="#">MEHR ERFAHREN</a></article>
</section>

<section class="stats">
  <svg class="waves" width="1200" height="335" viewBox="0 0 1200 335"><g fill="none" stroke="#2a2a2a" stroke-width="1"><path d="M0 120C300 40 500 220 800 140S1100 60 1200 110"/><path d="M0 150C300 70 500 250 800 170S1100 90 1200 140"/><path d="M0 180C300 100 500 280 800 200S1100 120 1200 170"/><path d="M0 210C300 130 500 310 800 230S1100 150 1200 200"/><path d="M0 240C300 160 500 340 800 260S1100 180 1200 230"/></g></svg>
  <div class="stat" style="left:121px">
    <svg width="190" height="190" viewBox="0 0 190 190"><circle cx="95" cy="95" r="91" fill="none" stroke="#fff" stroke-width="4"/><path d="M95 4A91 91 0 1 1 12 132" fill="none" stroke="#66bb2e" stroke-width="5"/></svg>
    <div class="over hand">ÜBER</div><div class="num"><small>+</small>56</div>
    <div class="label hand">JAHRE ERFAHRUNG</div>
  </div>
  <div class="stat" style="left:505px">
    <svg width="190" height="190" viewBox="0 0 190 190"><circle cx="95" cy="95" r="91" fill="none" stroke="#fff" stroke-width="4"/><path d="M95 4A91 91 0 1 1 5 110" fill="none" stroke="#66bb2e" stroke-width="5"/></svg>
    <div class="over hand">ZUFRIEDENE</div><div class="num"><small>+</small>1547</div>
    <div class="label hand">KUNDEN</div>
  </div>
  <div class="stat" style="left:887px">
    <svg width="190" height="190" viewBox="0 0 190 190"><circle cx="95" cy="95" r="91" fill="none" stroke="#fff" stroke-width="4"/><path d="M95 4A91 91 0 1 1 30 158" fill="none" stroke="#66bb2e" stroke-width="5"/></svg>
    <div class="over hand">MEHR ALS</div><div class="num">65<span class="unit">Mio.+</span></div>
    <div class="label hand">BINDUNGEN</div>
  </div>
</section>

<section class="gallery">
  <h2 class="section-title">UNSERE GALERIE</h2>
  <div class="tabs">
    <span class="active hand" style="left:25px">KALENDER</span>
    <span class="hand" style="left:150px">BÜCHER UND LOSEBLATTWERKE</span>
    <span class="hand" style="left:430px">EXKLUSIVE PRODUKTION</span>
  </div>

  <div class="tile" style="left:122px;top:199px"><div class="thumb" role="img" aria-label="Gestanzter Kalender in Skateboard-Form" style="background:linear-gradient(180deg,#fff 0%,#2a2a2a 20%,#d24a2c 55%,#2c5fa8 85%,#fff)"></div><h4 class="hand">STANZKALENDER</h4></div>
  <div class="tile" style="left:284px;top:199px"><div class="thumb" role="img" aria-label="Bunt illustrierte Kunstkalenderseite" style="background:linear-gradient(135deg,#f3a53b,#e24a6a 40%,#3a8fd4 70%,#f6d34a)"></div><h4 class="hand">KUNSTKALENDER MIT PRÄGUNG</h4></div>
  <div class="tile" style="left:447px;top:199px"><div class="thumb" role="img" aria-label="Aufgestellter Tischkalender mit Hardcover" style="background:linear-gradient(135deg,#f4f4f4,#c5c7cc 50%,#8a8f99)"></div><h4 class="hand">TISCHKALENDER</h4><p>mit Hardcover</p></div>
  <div class="tile" style="left:609px;top:199px"><div class="thumb" role="img" aria-label="Tischkalender mit Tierfoto" style="background:linear-gradient(160deg,#6d9a44,#b7a27a 50%,#d8dde6)"></div><h4 class="hand">KLASSISCHER TISCHKALENDER</h4><p>mit Ring-Wire-Bindung und Perforation</p></div>
  <div class="tile" style="left:772px;top:199px"><div class="thumb" role="img" aria-label="Dreimonatskalender mit Datumsraster" style="background:linear-gradient(180deg,#f5f7fa,#dfe7f2 50%,#c9d6ea)"></div><h4 class="hand">3-4-MONATSKALENDER</h4><p>mit Datumsschieber</p></div>
  <div class="tile" style="left:934px;top:199px"><div class="thumb" role="img" aria-label="Kalender mit farbig gestaffelten Monatsblättern" style="background:linear-gradient(180deg,#2d6fb8,#2fa0a0 35%,#6bb84a 60%,#e6c23a)"></div><h4 class="hand">KALENDER</h4><p>mit gestaffelten Monatsblättern</p></div>

  <div class="tile" style="left:122px;top:446px"><div class="thumb" role="img" aria-label="Weißer Tischkalender mit Doppelherz-Aufsteller" style="background:linear-gradient(135deg,#fafafa,#dcdcdc 60%,#bdbdbd)"></div><h4 class="hand">TISCHKALENDER</h4><p>mit Doppelherz-Aufsteller</p></div>
  <div class="tile" style="left:284px;top:446px"><div class="thumb" role="img" aria-label="Kalender mit individueller Werbefläche" style="background:linear-gradient(160deg,#c9c9c9,#e2d2c2 50%,#9a9a9a)"></div><h4 class="hand">KALENDER</h4><p>mit individueller Werbung</p></div>
  <div class="tile" style="left:447px;top:446px"><div class="thumb" role="img" aria-label="Klappkalender mit Food-Fotografie" style="background:linear-gradient(150deg,#f3f3f3,#c8452e 45%,#e2b04a 70%,#f3f3f3)"></div><h4 class="hand">KLAPPKALENDER</h4><p>gefalzt</p></div>
  <div class="tile" style="left:609px;top:446px"><div class="thumb" role="img" aria-label="Achteckiger Stanzkalender mit Unterwassermotiv" style="background:linear-gradient(180deg,#f2f2f2,#5fb6e6 25%,#1d5fa0 75%,#f2f2f2)"></div><h4 class="hand">STANZKALENDER</h4></div>
  <div class="tile" style="left:772px;top:446px"><div class="thumb" role="img" aria-label="Panoramakalender mit Berglandschaft" style="background:linear-gradient(180deg,#8a6a4a 0%,#f0f0f0 30%,#6f8fb8 55%,#3b4a5a 80%,#eeeeee)"></div><h4 class="hand">PANORAMAKALENDER</h4><p>Format: 160 x 55 cm</p></div>
  <div class="tile" style="left:934px;top:446px"><div class="thumb" role="img" aria-label="Blau-weiße gefalzte Tischkarte" style="background:linear-gradient(160deg,#f5f5f5 40%,#2b6fd0 75%,#dfe3e8)"></div><h4 class="hand">KALENDER MIT KLAPPE</h4></div>

  <a class="btn" href="#">Alle Bilder</a>
</section>

<section class="cta">
  <svg width="1200" height="294" viewBox="0 0 1200 294" style="position:absolute;left:0;top:0"><g fill="none" stroke="#5aa927" stroke-width="1.5"><path d="M0 210C120 200 200 150 260 60"/><path d="M0 240C140 230 230 170 290 70"/><path d="M900 294C1000 200 1100 120 1200 100"/><path d="M940 294C1030 220 1120 150 1200 135"/></g></svg>
  <h2>PLANEN SIE MIT ZIEL. ENTDECKEN SIE DIE<br>KALENDERBINDUNG, DIE ZU IHNEN PASST.</h2>
  <a class="btn" href="#">Jetzt starten</a>
</section>

<footer class="site-footer">
  <div class="brand">VELBRIN</div>
  <p class="footer-about">Der Druckweiterverarbeiter Velbrin ist eine der größten Kalenderfabriken Deutschlands, mit vier vollautomatischen Kalenderlinien.</p>

  <div class="fcol" style="left:322px">
    <h5>SCHNELLZUGRIFF</h5>
    <ul><li>Start</li><li>Unternehmen</li><li>Bindungen</li><li>Exklusiv</li><li>Galerie</li><li>Service</li></ul>
  </div>
  <div class="fcol contact" style="left:468px">
    <h5>KONTAKT</h5>
    <ul>
      <li><span class="ico"><svg width="12" height="12" viewBox="0 0 12 12"><path d="M2 1h3l1 3-2 1a7 7 0 0 0 3 3l1-2 3 1v3c-6 0-9-3-9-9z" fill="none" stroke="#e5322a"/></svg></span>+ 49 (8561) 4720-0</li>
      <li><span class="ico"><svg width="12" height="10" viewBox="0 0 12 10"><rect x=".5" y=".5" width="11" height="9" fill="none" stroke="#e5322a"/><path d="M.5 .5l5.5 5 5.5-5" fill="none" stroke="#e5322a"/></svg></span>info@velbrin-gmbh.example</li>
      <li><span class="ico"><svg width="12" height="12" viewBox="0 0 12 12"><circle cx="6" cy="6" r="5.5" fill="none" stroke="#e5322a"/><path d="M.5 6h11M6 .5c-3 3-3 8 0 11M6 .5c3 3 3 8 0 11" fill="none" stroke="#e5322a"/></svg></span>info@velbrin-gmbh.example</li>
    </ul>
  </div>
  <div class="fcol social" style="left:704px">
    <h5>FOLGEN SIE UNS</h5>
    <ul>
      <li><span class="ico"><svg width="8" height="8"><rect width="8" height="8" fill="#e5322a"/></svg></span>Faceboard</li>
      <li><span class="ico"><svg width="8" height="8"><rect width="8" height="8" fill="#e5322a"/></svg></span>Pictogram</li>
      <li><span class="ico"><svg width="8" height="8"><rect width="8" height="8" fill="#e5322a"/></svg></span>Chirper</li>
    </ul>
  </div>
  <div class="fcol newsletter" style="left:865px">
    <h5>NEWSLETTER</h5>
    <div class="field">E-Mail</div>
    <a class="btn" href="#">Abonnieren</a>
  </div>

  <div class="footer-bar">
    <span>2025 Velbrin GmbH &amp; Co. KG – Ringwire-Bindungen – Drahtkammbindungen – Kalenderbindungen – Auenfeld.</span>
    <nav><a href="#">Unternehmen</a><a href="#">Datenschutz</a><a href="#">AGB</a></nav>
  </div>
</footer>

</body>
</html>
```